Website for PeakWave Functional Training

We would like to launch a website for our boutique gym, PeakWave Functional Training. We'd like the website to have a lot of lime green which is one of our colors in our logo. The website will have a description of our workouts, membership, free trial class and location information.

Target Market(s)

Fitness enthusiasts, health conscious people, target ages 20-65, people looking to get fit and healthy, people looking to lose weight

Industry/Entity Type

Gym

Coding

Coded - Design and coding required

Number of Pages Required

1 page

Font styles to use
Serif

Colors
9ccb3b
34a7d8

Requirements
Must have
• A lot of lime green to match our logo. Let the website be fun, eye catchy. Our phone number which is 555-014-7391 to be easily dialed directly from our website.
Nice to have
• We would like to include this verbiage:
• -The Most FUN 1 hour workout
• -Affordable personal training/group training
• -Individualized workout programs
• -FUN workouts delivering results
• -Turn ON fat burn-The Most FUN 1 hour workout
• -Turn ON fat burning "EPOC" after burn
• We want our website to be easily seen on smart phones, iPads, Androids
Should not have
• Font that is hard on the eyes

```html
<!DOCTYPE html>
<html lang="en">
<head>
<meta charset="utf-8">
<title>PeakWave Functional Training</title>
<link rel="stylesheet" href="https://fonts.googleapis.com/css2?family=Oswald:wght@400;500;600&family=Raleway:wght@600;700&family=Open+Sans:wght@400;600;700&display=swap">
<style>
:root{
  --lime:#9ccb3b;
  --lime-dark:#86b52c;
  --lime-light:#b5dc5a;
  --blue:#34a7d8;
  --nav-active:#4fb7c9;
  --ink:#333;
  --muted:#666;
  --white:#fff;
  --dark:#2b2b2b;
  --footer:#7fab2f;
}
*{box-sizing:border-box;margin:0;padding:0}
html,body{width:1200px;height:4839px;overflow:hidden}
body{font-family:"Open Sans",Arial,sans-serif;color:var(--ink);background:var(--white);position:relative}
a{color:inherit;text-decoration:none}
.ph{display:block}

/* header */
.site-header{height:97px;position:relative;background:var(--white)}
.brand{position:absolute;left:50px;top:18px;display:flex;align-items:center;gap:12px}
.brand-dot{width:26px;height:26px;border-radius:50%;background:var(--lime)}
.brand-name{font-family:"Raleway",sans-serif;font-weight:700;color:var(--lime);font-size:22px;line-height:26px;width:200px}
.appointment{position:absolute;right:150px;top:14px;text-align:left}
.appointment span{display:block;color:var(--lime);font-size:21px;line-height:28px}
.appointment a{display:flex;align-items:center;gap:8px;font-family:"Oswald",sans-serif;font-size:26px;color:var(--ink);line-height:34px}

/* nav */
.main-nav{height:55px;background:var(--lime);display:flex;padding-left:48px}
.main-nav a{color:var(--white);font-size:17px;font-weight:600;line-height:55px;padding:0 22px}
.main-nav a.active{background:var(--nav-active)}

/* hero */
.hero{height:506px;position:relative;background:linear-gradient(100deg,#3a3c3e 0%,#6b6e70 40%,#9a9690 70%,#4a4a4a 100%)}
.hero-copy{position:absolute;left:115px;top:160px;font-family:"Oswald",sans-serif;font-weight:500}
.hero-copy .line1{color:var(--lime);font-size:74px;line-height:84px}
.hero-copy .line2{color:var(--white);font-size:58px;line-height:64px}
.hero-arrow{position:absolute;top:230px}
.hero-arrow.prev{left:70px}.hero-arrow.next{right:70px}

/* welcome */
.welcome{height:600px;position:relative;background:radial-gradient(ellipse at 30% 60%,#d6ef95 0%,var(--lime-light) 35%,var(--lime) 75%)}
.welcome h1{font-family:"Oswald",sans-serif;font-weight:500;color:var(--white);font-size:44px;text-align:center;padding-top:30px}
.welcome .intro{font-family:"Oswald",sans-serif;font-style:italic;font-size:17px;color:#222;text-align:center;width:720px;margin:8px auto 0;line-height:24px}
.welcome-photo{position:absolute;left:194px;top:165px;width:322px;height:435px;background:linear-gradient(180deg,#e9f6cc 0%,#e45a9a 55%,#2b2b2b 100%);border-radius:160px 160px 0 0}
.welcome-text{position:absolute;left:532px;top:268px;width:600px;color:var(--white)}
.welcome-text h2{font-family:"Raleway",sans-serif;font-size:31px;margin-bottom:18px}
.welcome-text p{font-size:16px;line-height:24px;margin-bottom:22px}
.btn-blue{display:inline-block;background:var(--blue);color:var(--white);font-family:"Raleway",sans-serif;font-weight:700;font-size:22px;padding:8px 20px;margin-left:32px}

/* feature rows */
.feature{position:relative}
.feature.light{background:var(--white)}
.feature.blue{background:var(--blue);color:var(--white)}
.feature .text{position:absolute;width:520px}
.feature h3{font-family:"Raleway",sans-serif;font-weight:700;font-size:31px;line-height:40px;margin-bottom:18px}
.feature.light h3{color:var(--blue)}
.feature p{font-size:15.5px;line-height:24px;margin-bottom:26px}
.feature.light p{color:var(--muted)}
.btn-outline{display:inline-block;font-size:17px;padding:7px 20px;border:2px solid var(--lime)}
.feature.light .btn-outline{color:var(--ink)}
.feature.blue .btn-outline{color:var(--white)}
.feature .photo{position:absolute;width:492px;height:310px}

/* testimonials */
.testimonials{height:478px;position:relative;background:linear-gradient(180deg,#3b3b3b,#242424);color:var(--white);text-align:center}
.testimonials h2{font-family:"Oswald",sans-serif;font-weight:500;font-size:40px;padding-top:28px}
.avatar{width:130px;height:130px;border-radius:50%;background:#e7c7b8;border:5px solid var(--white);margin:28px auto 0}
.quote{width:900px;margin:36px auto 0;font-size:19px;line-height:30px}
.quote .name{color:var(--blue)}
.dots{margin-top:40px;display:flex;justify-content:center;gap:8px}
.dots i{width:10px;height:10px;border-radius:50%;background:#888}
.dots i.on{background:var(--blue)}

/* gallery */
.gallery{height:574px;background:var(--white)}
.gallery h2{font-family:"Oswald",sans-serif;font-weight:500;font-size:40px;text-align:center;padding-top:40px}
.gallery-grid{display:grid;grid-template-columns:repeat(3,297px);gap:23px 26px;position:absolute;left:135px;top:3981px}
.gallery-grid .ph{height:177px;border:3px solid var(--white);outline:1px solid #ccc}

/* contact */
.contact{height:361px;background:var(--lime);color:var(--white);text-align:center;position:relative}
.contact h2{font-family:"Oswald",sans-serif;font-weight:500;font-size:40px;padding-top:35px}
.contact .sub{font-family:"Oswald",sans-serif;font-size:19px}
.contact-item{position:absolute;top:180px;width:300px;margin-left:-150px}
.contact-item .icon{width:70px;height:70px;border:2px solid var(--white);border-radius:50%;margin:0 auto 20px;display:flex;align-items:center;justify-content:center}
.contact-item .label{font-size:16px;font-weight:700;line-height:22px}
.contact-item .phone{font-family:"Oswald",sans-serif;font-size:27px;font-weight:500}
.site-footer{height:65px;background:var(--footer);color:#e9f4d2;font-size:14px;text-align:center;line-height:65px}
</style>
</head>
<body>
<header class="site-header">
  <div class="brand"><span class="brand-dot"></span><span class="brand-name">PeakWave Functional Training</span></div>
  <div class="appointment">
    <span>Make an appointment</span>
    <a href="tel:5550147391"><svg width="20" height="20" viewBox="0 0 24 24"><path fill="#9ccb3b" d="M6.6 10.8a15 15 0 0 0 6.6 6.6l2.2-2.2a1 1 0 0 1 1-.25 11 11 0 0 0 3.6.6 1 1 0 0 1 1 1V20a1 1 0 0 1-1 1A17 17 0 0 1 3 4a1 1 0 0 1 1-1h3.5a1 1 0 0 1 1 1 11 11 0 0 0 .6 3.6 1 1 0 0 1-.25 1z"/></svg>555-014-7391</a>
  </div>
</header>
<nav class="main-nav">
  <a class="active" href="#">Home</a><a href="#">Services</a><a href="#">About us</a><a href="#">Media Gallery</a><a href="#">References</a><a href="#">Blog</a><a href="#">Fitness AZ</a><a href="#">Contact</a>
</nav>

<section class="hero" role="img" aria-label="Athlete lifting dumbbells on a bench in a gym">
  <div class="hero-copy"><div class="line1">Power ON</div><div class="line2">The Best HIIT Workout</div></div>
  <svg class="hero-arrow prev" width="20" height="36" viewBox="0 0 20 36"><path d="M16 3 3 18l13 15" fill="none" stroke="#fff" stroke-width="3"/></svg>
  <svg class="hero-arrow next" width="20" height="36" viewBox="0 0 20 36"><path d="M4 3l13 15L4 33" fill="none" stroke="#fff" stroke-width="3"/></svg>
</section>

<section class="welcome">
  <h1>Welcome to PeakWave Functional Training</h1>
  <p class="intro">Lorem ipsum dolor sit amet, consectetuer adipiscing elit. Aenean commodo ligula eget dolor. Aenean massa. Cum sociis natoque penatibus et magnis dis parturient</p>
  <div class="welcome-photo ph" role="img" aria-label="Cheerful woman in pink top raising her arms"></div>
  <div class="welcome-text">
    <h2>The Most FUN 1 hour workout</h2>
    <p>Lorem ipsum dolor sit amet, consectetuer adipiscing elit, sed diam nonummy nibh euismod tincidunt ut laoreet dolore magna aliquam erat volutpat. Ut wisi enim ad minim veniam, quis nostrud exerci tation ullamcorper suscipit lobortis nisl ut aliquip ex ea commodo consequat.</p>
    <p>Lorem ipsum dolor sit amet, consectetuer adipiscing elit, sed diam nonummy nibh euismod tincidunt ut laoreet dolore magna aliquam erat volutpat.</p>
    <a class="btn-blue" href="#">Contact Us</a>
  </div>
</section>

<section class="feature light" style="height:413px">
  <div class="text" style="left:55px;top:48px">
    <h3>Affordable personal training and group training</h3>
    <p>Lorem ipsum dolor sit amet, consectetuer adipiscing elit, sed diam nonummy nibh euismod tincidunt ut laoreet dolore magna aliquam erat volutpat. Ut wisi enim ad minim veniam, quis nostrud exerci tation ullamcorper suscipit lobortis nisl ut aliquip ex ea commodo consequat.</p>
    <a class="btn-outline" href="#">Read More</a>
  </div>
  <div class="photo ph" style="left:655px;top:42px;background:linear-gradient(135deg,#2e3a48,#6a7a8c 50%,#3a3f45)" role="img" aria-label="Trainer coaching a client on a gym machine"></div>
</section>

<section class="feature blue" style="height:410px">
  <div class="photo ph" style="left:55px;top:45px;background:linear-gradient(180deg,#cfe4f0,#9fc0d4 55%,#2a2a2a)" role="img" aria-label="Man doing push-ups on kettlebells"></div>
  <div class="text" style="left:623px;top:62px;width:560px">
    <h3>Individualized workout programs</h3>
    <p>Lorem ipsum dolor sit amet, consectetuer adipiscing elit, sed diam nonummy nibh euismod tincidunt ut laoreet dolore magna aliquam erat volutpat. Ut wisi enim ad minim veniam, quis nostrud exerci tation ullamcorper suscipit lobortis nisl ut aliquip ex ea commodo consequat.</p>
    <a class="btn-outline" href="#">Read More</a>
  </div>
</section>

<section class="feature light" style="height:429px">
  <div class="text" style="left:55px;top:50px">
    <h3>FUN workouts delivering results</h3>
    <p>Lorem ipsum dolor sit amet, consectetuer adipiscing elit, sed diam nonummy nibh euismod tincidunt ut laoreet dolore magna aliquam erat volutpat. Ut wisi enim ad minim veniam, quis nostrud exerci tation ullamcorper suscipit lobortis nisl ut aliquip ex ea commodo consequat.</p>
    <a class="btn-outline" href="#">Read More</a>
  </div>
  <div class="photo ph" style="left:655px;top:57px;background:linear-gradient(135deg,#f1e7df,#d9c7b8 50%,#6fb5d9)" role="img" aria-label="Group fitness class stretching arms"></div>
</section>

<section class="feature blue" style="height:410px">
  <div class="photo ph" style="left:55px;top:48px;background:linear-gradient(180deg,#e9e6dc,#c9c2b0 50%,#7fb04a)" role="img" aria-label="Women exercising on fitness balls"></div>
  <div class="text" style="left:623px;top:55px;width:560px">
    <h3>Turn ON fat burn-The Most FUN 1 hour workout</h3>
    <p>Lorem ipsum dolor sit amet, consectetuer adipiscing elit, sed diam nonummy nibh euismod tincidunt ut laoreet dolore magna aliquam erat volutpat. Ut wisi enim ad minim veniam, quis nostrud exerci tation ullamcorper suscipit lobortis nisl ut aliquip ex ea commodo consequat.</p>
    <a class="btn-outline" href="#">Read More</a>
  </div>
</section>

<section class="feature light" style="height:441px">
  <div class="text" style="left:55px;top:55px">
    <h3>Turn ON fat burning “EPOC” after burn</h3>
    <p>Lorem ipsum dolor sit amet, consectetuer adipiscing elit, sed diam nonummy nibh euismod tincidunt ut laoreet dolore magna aliquam erat volutpat. Ut wisi enim ad minim veniam, quis nostrud exerci tation ullamcorper suscipit lobortis nisl ut aliquip ex ea commodo consequat.</p>
    <a class="btn-outline" href="#">Read More</a>
  </div>
  <div class="photo ph" style="left:655px;top:62px;background:linear-gradient(180deg,#f4f4f4,#e3c3b3 45%,#d6d6d6)" role="img" aria-label="Waist measured with a tape measure"></div>
</section>

<section class="testimonials">
  <h2>Testimonials</h2>
  <div class="avatar" role="img" aria-label="Client portrait"></div>
  <p class="quote">Lorem ipsum dolor sit amet, consectetuer adipiscing elit. Aenean commodo ligula eget dolor. Aenean massa. Cum sociis natoque... <span class="name">Lena</span></p>
  <div class="dots"><i class="on"></i><i></i><i></i></div>
</section>

<section class="gallery">
  <h2>Media Gallery</h2>
  <div class="gallery-grid">
    <div class="ph" style="background:linear-gradient(135deg,#d8e6c0,#8fae6a)" role="img" aria-label="Group training session"></div>
    <div class="ph" style="background:linear-gradient(135deg,#3a3a3a,#8a6a5a)" role="img" aria-label="Muscular athlete"></div>
    <div class="ph" style="background:linear-gradient(135deg,#2a2a2a,#6a7280)" role="img" aria-label="Man lifting weights"></div>
    <div class="ph" style="background:linear-gradient(135deg,#cfd6dc,#8b97a3)" role="img" aria-label="Gym floor with machines"></div>
    <div class="ph" style="background:linear-gradient(135deg,#b9c6d2,#5d6b78)" role="img" aria-label="Woman stretching on a mat"></div>
    <div class="ph" style="background:linear-gradient(135deg,#d5d8da,#6f7479)" role="img" aria-label="Weight training area"></div>
  </div>
</section>

<section class="contact">
  <h2>Let´s Talk</h2>
  <p class="sub">Visit Us, Give us a call, write as an email</p>
  <div class="contact-item" style="left:232px">
    <div class="icon"><svg width="26" height="32" viewBox="0 0 24 30"><path d="M12 1a9 9 0 0 0-9 9c0 7 9 18 9 18s9-11 9-18a9 9 0 0 0-9-9z" fill="none" stroke="#fff" stroke-width="2"/><circle cx="12" cy="10" r="3" fill="#fff"/></svg></div>
    <p class="label">Lorem ipsum dolor sit amet<br>consetetur sadipscing elitr</p>
  </div>
  <div class="contact-item" style="left:600px">
    <div class="icon"><svg width="28" height="28" viewBox="0 0 24 24"><path fill="#fff" d="M6.6 10.8a15 15 0 0 0 6.6 6.6l2.2-2.2a1 1 0 0 1 1-.25 11 11 0 0 0 3.6.6 1 1 0 0 1 1 1V20a1 1 0 0 1-1 1A17 17 0 0 1 3 4a1 1 0 0 1 1-1h3.5a1 1 0 0 1 1 1 11 11 0 0 0 .6 3.6 1 1 0 0 1-.25 1z"/></svg></div>
    <a class="phone" href="tel:5550147391">555-014-7391</a>
  </div>
  <div class="contact-item" style="left:968px">
    <div class="icon"><svg width="30" height="22" viewBox="0 0 30 22"><rect x="1" y="1" width="28" height="20" fill="none" stroke="#fff" stroke-width="2"/><path d="M1 1l14 11L29 1" fill="none" stroke="#fff" stroke-width="2"/></svg></div>
    <a class="label" href="mailto:info@peakwavefit.example">info@peakwavefit.example</a>
  </div>
</section>
<footer class="site-footer">© Copyright 2017 . All rights reserved.</footer>
</body>
</html>
```